Medical supplies company needs a catalogue re-design

Our present catalogue is spread over a number of pages but this needs to be reduced. 4-5 images would require to be on each page. It needs to be professional, simple and elegant. The photos and descriptors need to be adjacent to each other. It should be able to be emailed conventionally as an e-catalogue without it being compressed. an email with existing catalogue will be emailed to anyone interested.
https://www.filevarn.com/s/82kqtb5wzrmuyap/consumables%20photos%20and%20descriptions.pdf?dl=0
Target Market(s)
medical practices, hospitals
Industry/Entity Type
Medical Supply

```html
<!DOCTYPE html>
<html lang="en">
<head>
<meta charset="utf-8">
<title>Wound Care – Kelora Medical Catalogue</title>
<link href="https://fonts.googleapis.com/css2?family=Bitter:wght@700;800&family=Noto+Serif:ital,wght@0,400;0,700;1,400&display=swap" rel="stylesheet">
<style>
  :root {
    --brand-blue: #1a9fdc;
    --heading-blue: #1590cf;
    --brand-red: #d9232e;
    --ink: #1c1c1c;
    --panel: rgba(255,255,255,0.78);
    --sky-edge: #19ade6;
    --sky-mid: #bfe8f8;
  }
  * { margin: 0; padding: 0; box-sizing: border-box; }
  html, body { width: 848px; height: 1200px; overflow: hidden; }
  body {
    position: relative;
    font-family: "Noto Serif", Georgia, serif;
    color: var(--ink);
    background:
      radial-gradient(ellipse 620px 760px at 470px 470px, #ffffff 0%, #f4fbfe 35%, var(--sky-mid) 70%, var(--sky-edge) 100%);
  }
  .page-title {
    position: absolute; left: 40px; top: 42px;
    font-family: "Bitter", serif; font-weight: 800;
    font-size: 39px; color: #000; letter-spacing: 0.3px;
  }
  .title-rule {
    position: absolute; left: 284px; top: 76px; width: 524px; height: 3px;
    background: var(--brand-blue);
  }
  .brand {
    position: absolute; right: 40px; top: 20px;
    display: flex; align-items: center; gap: 8px;
    font-family: "Bitter", serif; font-weight: 800;
    font-size: 30px; color: var(--brand-red); letter-spacing: 1px;
  }
  .brand-dot { width: 26px; height: 26px; border-radius: 50%; background: var(--brand-red); }

  .product-photo {
    position: absolute; left: 40px; width: 253px;
    border: 3px solid var(--brand-blue);
  }
  .product-info {
    position: absolute; left: 301px;
    background: var(--panel);
    padding: 0 6px 6px 0;
  }
  .product-name {
    font-family: "Bitter", serif; font-weight: 700;
    font-size: 18px; line-height: 22px; color: var(--heading-blue);
    margin-bottom: 2px;
  }
  .features { list-style: none; font-size: 12.6px; line-height: 17px; }
  .features li { position: relative; padding-left: 24px; }
  .features li::before {
    content: ""; position: absolute; left: 10px; top: 4px;
    width: 7px; height: 9px; background: var(--brand-blue);
    clip-path: polygon(50% 0, 100% 50%, 50% 100%, 0 50%);
  }
  .pack { font-size: 12.6px; line-height: 17px; font-style: italic; }
  .pack.plain { font-style: normal; font-size: 14px; line-height: 19px; }
  .pack b { font-style: normal; }
</style>
</head>
<body>
  <h1 class="page-title">Wound Care</h1>
  <div class="title-rule"></div>
  <div class="brand"><span>KELORA</span><span class="brand-dot"></span></div>

  <div class="product-photo" role="img" aria-label="Photo of three rolls of unbleached crepe elastic bandage in clear wrappers" style="top:120px;height:143px;background:linear-gradient(135deg,#e9e6dc,#d8d3c4 50%,#ece9e1);"></div>
  <section class="product-info" style="top:116px;width:355px;height:104px;">
    <h2 class="product-name">Unbleached Crepe Elastic Bandages<br>(7.5 cm x 4.5 m, 10cm x 4.5 m)</h2>
    <ul class="features">
      <li>Ideal for holding dressings in place</li>
      <li>can be used for strapping</li>
    </ul>
    <p class="pack">(12 rolls per box)</p>
  </section>

  <div class="product-photo" role="img" aria-label="Photo of a red cohesive bandage roll" style="top:330px;height:142px;background:linear-gradient(90deg,#ffffff,#f6f6f6 20%,#e9524f 35%,#f05a57 70%,#ffffff 90%);"></div>
  <section class="product-info" style="top:326px;width:483px;height:114px;">
    <h2 class="product-name">Cohesive Bandages (7.5 cm x 4.5 m, 10cm x 4.5 m)</h2>
    <ul class="features">
      <li>offers compression to support a joint or muscle</li>
      <li>secures wound dressings &amp; is painless when removed</li>
      <li>secures to itself &amp; can be torn by hand</li>
      <li>won’t leave any sticky residue</li>
      <li>conforms to all body contours</li>
    </ul>
  </section>

  <div class="product-photo" role="img" aria-label="Photo of a non woven adhesive wound dressing pack beside the dressing" style="top:538px;height:155px;background:linear-gradient(90deg,#f4f5f7,#eceef2 55%,#f8f8f8);"></div>
  <section class="product-info" style="top:536px;width:507px;height:202px;">
    <h2 class="product-name">Non Woven Adhesive Wound Dressing</h2>
    <ul class="features">
      <li>Convenient all in one sterile dressing that can be used for a large range of wound and skin lesions.</li>
      <li>It is well absorbent and non adherent to wounds with minimal risk of skin reactions.</li>
      <li>It protects open wounds and reduces wound infection</li>
      <li>Not waterproof</li>
      <li>Used for both surgical wound care and post traumatic wound closure</li>
    </ul>
    <p class="pack">50 pcs per box (6cm by 8cm)<br>100 pcs per box (10cm by 10cm)<br><b>Sizes:</b> <span style="font-style:normal">6cm by 8cm, 10cm by 10cm</span></p>
  </section>

  <div class="product-photo" role="img" aria-label="Photo of an extra thin hydrocolloid dressing pack beside the beige dressing" style="top:760px;height:165px;background:linear-gradient(90deg,#f3f4f6,#eceef1 58%,#ead9b6 70%,#e8d6b2 90%,#f4f4f4);"></div>
  <section class="product-info" style="top:758px;width:510px;background:none;">
    <h2 class="product-name">Hydrocolloid Dressing (extra thin)</h2>
    <ul class="features">
      <li>This is for low or moderate exudate wounds. Suitable for venous ulcers, bed sores, superficial burns, post operative wounds and healing of chronic ulcers.</li>
      <li>Provides a waterproof barrier over the dressing.</li>
      <li>Does not damage newly formed tissues on removal</li>
      <li>Can be cut to fit</li>
    </ul>
    <p class="pack" style="font-size:14px;line-height:19px;">Needs to be changed every two to three days</p>
    <p class="pack plain">7.5cm by 7.5cm (25 pcs per box)<br>and 10cm by 10cm (10 pcs per box)</p>
  </section>

  <div class="product-photo" role="img" aria-label="Photo of a box of plaster rolls with red and white plastic tins" style="top:992px;height:167px;background:linear-gradient(135deg,#f7f9fb,#e6eef6 50%,#f2d4d4 75%,#ffffff);"></div>
  <section class="product-info" style="top:990px;width:480px;background:none;">
    <h2 class="product-name">Transparent Plaster With Plastic Tin</h2>
    <ul class="features">
      <li>Zinc oxide tape used for securing dresses, particularly along joints and contoured body parts.</li>
      <li>Comfortable and breathable</li>
      <li>Strong adhesion</li>
    </ul>
    <p class="pack">2.5 by 9m (12 per box)</p>
  </section>
</body>
</html>
```